Help a start up law firm make an impression! - Website

We are a property development and conveyancing law firm looking for some to design our website. The initial brief is for 6 pages with scope for on-going work.

Law firms are traditionally quite conservative and we want to break the mold. We want to come across as fun and modern, while still being professional.

A good example is https://quorrantlaw.com.au/. It's professional yet modern.
Updates

Another good site I like in the same industry: https://www.tindalemarshconveyancing.com.au/

Target Market(s)

Tech savy home buyers and sellers - generally 30 to 50 years old

Industry/Entity Type

Law Firm

Coding

Coded - Design and coding required

Number of Pages Required

5+ page

Font styles to use
Other font styles liked:
• No idea

Colors
f04a50

Requirements
Must have
• The elements set out in the design brief document

```html
<!DOCTYPE html>
<html lang="en">
<head>
<meta charset="utf-8">
<title>Hartwell Law – Jonas Merrow</title>
<link href="https://fonts.googleapis.com/css2?family=Arvo:wght@700&family=Montserrat:wght@300;400;500;600;700&family=Oswald:wght@400;500&family=Raleway:wght@400;500;600&display=swap" rel="stylesheet">
<style>
:root{
  --red:#d8394f;
  --red-soft:#e15870;
  --navy:#2b4460;
  --navy-deep:#12294a;
  --ink:#333;
  --grey:#555;
  --paper:#f7f7f7;
  --bar:#e3e3e3;
  --white:#fff;
}
*{margin:0;padding:0;box-sizing:border-box}
html,body{width:674px;height:1200px;overflow:hidden}
body{position:relative;background:var(--paper);font-family:"Raleway",sans-serif;color:var(--ink)}
.abs{position:absolute}

/* header */
.hero{left:0;top:0;width:674px;height:186px;background:linear-gradient(160deg,#4a6079 0%,#2f4863 55%,#24394f 100%)}
.hero-rule{left:0;top:57px;width:674px;height:1px;background:rgba(255,255,255,.15)}
.brand{left:14px;top:15px;font-family:"Arvo",serif;font-weight:700;font-size:21px;color:var(--white)}
.nav{left:197px;top:25px;display:flex;gap:12px;font-family:"Oswald",sans-serif;font-size:9px;color:var(--white)}
.nav .current{color:var(--red)}
.head-phone{left:542px;top:21px;display:flex;align-items:center;gap:6px;font-family:"Oswald",sans-serif;font-size:16px;color:var(--white)}
.hero-title{left:0;width:674px;top:74px;text-align:center;font-family:"Arvo",serif;font-weight:700;font-size:38px;letter-spacing:1px;color:var(--white)}
.hero-sub{left:0;width:674px;top:137px;text-align:center;font-size:11px;font-weight:600;color:var(--white)}

/* profile */
.portrait{left:99px;top:225px;width:176px;height:231px;background:linear-gradient(135deg,#5a4a3a 0%,#2a2622 60%,#1b1a1a 100%)}
.name{left:297px;top:224px;font-family:"Montserrat",sans-serif;font-weight:700;font-size:17px;color:var(--red);letter-spacing:.3px}
.role{left:298px;top:245px;font-family:"Montserrat",sans-serif;font-size:12px;color:var(--ink)}
.socials{display:flex;gap:4px}
.socials span{width:19px;height:19px;border-radius:50%;background:#6b6b6b;display:block}
.profile-social{left:486px;top:226px}
.bio{left:297px;top:268px;width:280px;font-size:7.6px;line-height:11px;text-align:justify;color:var(--grey)}
.contacts{left:297px;top:368px;list-style:none;font-size:11.5px;color:var(--ink)}
.contacts li{display:flex;align-items:center;gap:10px;height:19.6px}
.contacts svg{width:14px;height:14px;flex:none}
.profile-rule{left:275px;top:456px;width:308px;height:1.5px;background:var(--red)}
.sec-title{font-family:"Montserrat",sans-serif;font-weight:600;font-size:12px;color:var(--red)}
.quals-title{left:99px;top:470px}
.quals{left:99px;top:492px;width:226px;font-size:7.6px;line-height:11px;text-align:justify;color:var(--grey)}
.ach-title{left:347px;top:470px}
.achievements{left:347px;top:489px;list-style:none;font-size:7.6px;color:var(--grey)}
.achievements li{display:flex;align-items:center;gap:4px;height:14.5px}
.achievements svg{width:8px;height:8px}
.return{left:99px;top:630px;width:484px;height:30px;background:var(--red-soft);border-left:4px solid var(--red);border-radius:2px;box-shadow:0 2px 0 #b8304a}
.return-label{left:0;width:440px;top:9px;text-align:center;font-family:"Montserrat",sans-serif;font-weight:600;font-size:10px;letter-spacing:.5px;color:var(--white)}
.return-tab{right:0;top:0;width:44px;height:30px;background:var(--red);display:flex;align-items:center;justify-content:center}

/* contact */
.contact{left:0;top:700px;width:674px;height:320px;background:linear-gradient(180deg,#1c3554 0%,#20406a 50%,#142e51 100%)}
.contact-icon{left:321px;top:718px}
.contact-heading{left:0;width:674px;top:752px;text-align:center;font-family:"Montserrat",sans-serif;font-weight:300;font-size:21px;letter-spacing:1px;color:var(--white)}
.contact-heading b{color:var(--red);font-weight:700}
.deco-line{top:767px;height:1px;width:66px;background:rgba(255,255,255,.6)}
.deco-dot{top:764px;width:7px;height:7px;border:1px solid rgba(255,255,255,.7);border-radius:50%}
.field{background:var(--white);border-radius:2px;font-family:"Montserrat",sans-serif;font-size:6.5px;color:#888;padding:9px 7px}
.send{left:118px;top:956px;width:437px;height:24px;background:var(--red);border-radius:2px;text-align:center;line-height:24px;font-family:"Montserrat",sans-serif;font-weight:600;font-size:7px;color:var(--white)}
.notch{left:287px;top:996px}

/* footer */
.foot-title{top:1040px;font-family:"Montserrat",sans-serif;font-weight:600;font-size:10px;color:var(--red)}
.foot-title::after{content:"";display:block;width:14px;height:1.5px;background:var(--red);margin-top:5px}
.quick{left:55px;top:1064px;list-style:none;font-family:"Montserrat",sans-serif;font-size:8.5px;line-height:14.2px;color:var(--grey)}
.foot-contact{left:222px;top:1064px;list-style:none;font-family:"Montserrat",sans-serif;font-size:8.5px;color:var(--grey)}
.foot-contact li{display:flex;gap:8px;align-items:flex-start;margin-bottom:12px;line-height:11px}
.foot-contact svg{width:10px;height:10px;flex:none;margin-top:1px}
.foot-brand{left:450px;top:1062px;font-family:"Arvo",serif;font-weight:700;font-size:22px;color:#222}
.bottom-bar{left:0;top:1162px;width:674px;height:38px;background:var(--bar)}
.copyright{left:55px;top:14px;font-family:"Montserrat",sans-serif;font-weight:500;font-size:7.5px;color:#333}
.bottom-social{right:55px;top:9px}
</style>
</head>
<body>

<header class="hero abs">
  <div class="hero-rule abs"></div>
  <div class="brand abs">Hartwell Law</div>
  <nav class="nav abs">
    <span>Home</span><span>Conveyancing</span><span>Property Development</span><span>News &amp; Knowledge</span><span class="current">About us</span><span>Contact us</span>
  </nav>
  <div class="head-phone abs">
    <svg width="14" height="14" viewBox="0 0 24 24"><path d="M6 2l4 4-2.5 2.5a12 12 0 0 0 8 8L18 14l4 4-3 3C10 21 3 14 3 5z" fill="#d8394f"/></svg>
    (07) 3184 2270
  </div>
  <h1 class="hero-title abs">THE HARTWELL TEAM</h1>
  <p class="hero-sub abs">Challenging ourselves to bring new and original ways of thinking</p>
</header>

<main>
  <div class="portrait abs" role="img" aria-label="Portrait photo of Jonas Merrow in a suit"></div>
  <h2 class="name abs">JONAS MERROW</h2>
  <div class="role abs">FOUNDER</div>
  <div class="socials profile-social abs"><span></span><span></span><span></span><span></span></div>
  <p class="bio abs">Lorem Ipsum is simply dummy text of the printing and typesetting industry. Lorem Ipsum has been the industry's standard dummy text ever since the 1500s, when an unknown printer took a galley of type and scrambled it to make a type specimen book. It has survived not only five centuries, but also the leap into electronic typesetting, remaining essentially unchanged. It was popularised in the 1960s with the release of transfer sheets containing Lorem Ipsum passages, and more recently with desktop publishing software and page layout tools including versions of Lorem Ipsum.</p>
  <ul class="contacts abs">
    <li><svg viewBox="0 0 24 24"><path d="M6 2l4 4-2.5 2.5a12 12 0 0 0 8 8L18 14l4 4-3 3C10 21 3 14 3 5z" fill="#d8394f"/></svg>07 3184 2291</li>
    <li><svg viewBox="0 0 24 24"><rect x="7" y="2" width="10" height="20" rx="2" fill="none" stroke="#d8394f" stroke-width="2"/><circle cx="12" cy="18" r="1.2" fill="#d8394f"/></svg>0412 555 019</li>
    <li><svg viewBox="0 0 24 24"><rect x="2" y="5" width="20" height="14" fill="#d8394f"/><path d="M2 5l10 8 10-8" fill="none" stroke="#fff" stroke-width="1.5"/></svg>Email Jonas Merrow</li>
    <li><svg viewBox="0 0 24 24"><circle cx="12" cy="12" r="11" fill="#d8394f"/></svg>Connect with Jonas Merrow online</li>
  </ul>
  <div class="profile-rule abs"></div>

  <h3 class="sec-title quals-title abs">Qualifications and Experience</h3>
  <p class="quals abs">Lorem Ipsum is simply dummy text of the printing and typesetting industry. Lorem Ipsum has been the industry's standard dummy text ever since the 1500s, when an unknown printer took a galley of type and scrambled it to make a type specimen book. It has survived not only five centuries, but also the leap into electronic typesetting, remaining essentially unchanged. It was popularised in the 1960s with the release of transfer sheets containing Lorem Ipsum passages, and more recently with desktop publishing software and page layout tools including versions of Lorem Ipsum.</p>

  <h3 class="sec-title ach-title abs">Recent Achievements</h3>
  <ul class="achievements abs">
    <li><svg viewBox="0 0 10 10"><circle cx="5" cy="5" r="4.3" fill="none" stroke="#d8394f"/><path d="M4 3l2 2-2 2" fill="none" stroke="#d8394f"/></svg>Lorem ipsum dolor sit amet, consectetur adipiscing elit</li>
    <li><svg viewBox="0 0 10 10"><circle cx="5" cy="5" r="4.3" fill="none" stroke="#d8394f"/><path d="M4 3l2 2-2 2" fill="none" stroke="#d8394f"/></svg>Lorem ipsum dolor sit amet, consectetur adipiscing elit</li>
    <li><svg viewBox="0 0 10 10"><circle cx="5" cy="5" r="4.3" fill="none" stroke="#d8394f"/><path d="M4 3l2 2-2 2" fill="none" stroke="#d8394f"/></svg>Lorem ipsum dolor sit amet, consectetur adipiscing elit</li>
    <li><svg viewBox="0 0 10 10"><circle cx="5" cy="5" r="4.3" fill="none" stroke="#d8394f"/><path d="M4 3l2 2-2 2" fill="none" stroke="#d8394f"/></svg>Lorem ipsum dolor sit amet, consectetur adipiscing elit</li>
    <li><svg viewBox="0 0 10 10"><circle cx="5" cy="5" r="4.3" fill="none" stroke="#d8394f"/><path d="M4 3l2 2-2 2" fill="none" stroke="#d8394f"/></svg>Lorem ipsum dolor sit amet, consectetur adipiscing elit</li>
    <li><svg viewBox="0 0 10 10"><circle cx="5" cy="5" r="4.3" fill="none" stroke="#d8394f"/><path d="M4 3l2 2-2 2" fill="none" stroke="#d8394f"/></svg>Lorem ipsum dolor sit amet, consectetur adipiscing elit</li>
    <li><svg viewBox="0 0 10 10"><circle cx="5" cy="5" r="4.3" fill="none" stroke="#d8394f"/><path d="M4 3l2 2-2 2" fill="none" stroke="#d8394f"/></svg>Lorem ipsum dolor sit amet, consectetur adipiscing elit</li>
    <li><svg viewBox="0 0 10 10"><circle cx="5" cy="5" r="4.3" fill="none" stroke="#d8394f"/><path d="M4 3l2 2-2 2" fill="none" stroke="#d8394f"/></svg>Lorem ipsum dolor sit amet, consectetur adipiscing elit</li>
  </ul>

  <div class="return abs">
    <div class="return-label abs">RETURN TO OUR PEOPLE</div>
    <div class="return-tab abs">
      <svg width="22" height="16" viewBox="0 0 22 16"><path d="M9 1L1 7l8 6V9c6 0 9 2 12 6-1-6-4-10-12-10z" fill="#fff"/></svg>
    </div>
  </div>
</main>

<section class="contact abs"></section>
<svg class="contact-icon abs" width="32" height="30" viewBox="0 0 32 30" fill="none" stroke="#fff" stroke-width="1.3">
  <rect x="4" y="2" width="18" height="14"/><rect x="7" y="5" width="12" height="8"/><path d="M1 20h24l-3-4H4z"/><circle cx="24" cy="21" r="7"/><path d="M20 24l8-7"/>
</svg>
<div class="deco-dot abs" style="left:174px"></div>
<div class="deco-line abs" style="left:181px;width:61px"></div>
<div class="deco-line abs" style="left:440px;width:61px"></div>
<div class="deco-dot abs" style="left:501px"></div>
<h2 class="contact-heading abs">GET IN <b>TOUCH</b></h2>
<div class="field abs" style="left:118px;top:794px;width:212px;height:24px">FIRST NAME*</div>
<div class="field abs" style="left:345px;top:794px;width:210px;height:24px">LAST NAME*</div>
<div class="field abs" style="left:118px;top:833px;width:212px;height:24px">E-MAIL ADDRESS*</div>
<div class="field abs" style="left:345px;top:833px;width:210px;height:24px">PHONE NUMBER*</div>
<div class="field abs" style="left:118px;top:871px;width:437px;height:72px">MESSAGE</div>
<div class="send abs">SEND NOW</div>
<svg class="notch abs" width="100" height="25" viewBox="0 0 100 25">
  <path d="M0 25C20 25 22 3 50 3S80 25 100 25z" fill="#f7f7f7"/>
  <path d="M45 12l5 4 5-4" fill="none" stroke="#d8394f" stroke-width="1.3"/>
</svg>

<footer>
  <h4 class="foot-title abs" style="left:55px">QUICK LINKS</h4>
  <ul class="quick abs">
    <li>Home</li><li>Conveyancing</li><li>Property Development</li><li>News &amp; Knowledge</li><li>About us</li><li>Contact us</li>
  </ul>
  <h4 class="foot-title abs" style="left:239px">CONTACT US</h4>
  <ul class="foot-contact abs">
    <li><svg viewBox="0 0 10 10"><path d="M5 0a3.5 3.5 0 0 1 3.5 3.5C8.5 6 5 10 5 10S1.5 6 1.5 3.5A3.5 3.5 0 0 1 5 0z" fill="#d8394f"/><circle cx="5" cy="3.5" r="1.2" fill="#fff"/></svg><span>Level 2, 48 Wattle Street,<br>Kelvin Grove, Queensland 4059</span></li>
    <li style="margin-top:6px"><svg viewBox="0 0 10 10"><circle cx="5" cy="5" r="5" fill="#d8394f"/><path d="M3 2.5l1.3 1.3-.6.7a3.5 3.5 0 0 0 1.8 1.8l.7-.6L7.5 7 6.8 7.6C4.5 7.5 2.5 5.5 2.4 3.2z" fill="#fff"/></svg><span>(07) 3184 2270</span></li>
    <li style="margin-top:6px"><svg viewBox="0 0 10 10"><circle cx="5" cy="5" r="5" fill="#d8394f"/><rect x="2.5" y="3.2" width="5" height="3.6" fill="#fff"/></svg><span>hello@hartwelllaw.com.au</span></li>
  </ul>
  <div class="foot-brand abs">Hartwell Law</div>
  <div class="bottom-bar abs">
    <div class="copyright abs">© COPYRIGHT - 2017 &nbsp;| &nbsp;ALL RIGHTS RESERVED</div>
    <div class="socials bottom-social abs"><span></span><span></span><span></span><span></span></div>
  </div>
</footer>

</body>
</html>
```